Coffee bag + cups: retail packaging

Our is seeking new packaging for a new coffee shop concept. As part of this we need to design new packaging for our coffee products. For this request, we are seeking design layouts for our retail bags and a cup for to-go coffee. We are working with 3 logo versions (pending final approval).

Please reference this website to see the types of coffee bag packaging options, there's a variety of bag options. We'd like the bag to be a Gusseted Bag, size 3.625 x 9.6 x 2.3125. We want a matte laminated material, not shiny.
https://www.brellumpack.com/

BAG
We'd like to see options of a black bag, blue, and kraft paper. Reference attached example.

Below is the text for our current bags, you can use that for now. I've attached example of bags that I like. We will look to you for design thoughts.

[Front]
Logo
100% Tanzanian
12oz
Dark Roast
Ground

[Back]
Amber Ridge Farms was established in 1989 by Marcus Ellery, son of baseball legend Thomas Ellery, and his family in rural Tanzania.
Today the coffee brand is sourced exclusively from the Ellery farm and other small scale family owned farms in Tanzania and East Africa.
This international coffee initiative is designed to bring a greater share of coffee revenues to farmers through direct trade and help develop rural communities in East Africa.

Visit us at Kelvorabeans.com

[Left panel]

Brewing instructions: Lorem ipsum dolor sit amet, consectetur adipiscing elit, sed do eiusmod tempor incididunt ut labore et dolore magna aliqua.

[Right panel]

Leave blank

Cup Sleeve
[Front of sleeve]
Logo

To-go cup
[Front]
Logo

Target Market(s)

Specialty coffee lovers.

Font styles to use
Serif
Sans Serif

Colors

Designer to choose colors to be used in the design.

Requirements
Must have
• Examples of coffee bag packaging.
• Must have; logo, text, clear and elegant labeling. Simple but strong.

```html
<!DOCTYPE html>
<html lang="en">
<head>
<meta charset="utf-8">
<title>Amber Ridge Coffee – Retail Bag</title>
<link href="https://fonts.googleapis.com/css2?family=Arimo:wght@700&family=Cinzel:wght@400;600&family=Lato:wght@700&family=Marcellus&display=swap" rel="stylesheet">
<style>
  :root {
    --backdrop: #d3d3d4;
    --bag-black: #131416;
    --keyline: #e9e9e9;
    --brand-brown: #6b3513;
    --label-brown: #7a3a14;
    --band-blue: #1f4fb4;
    --label-white: #ffffff;
    --copy-white: #f2f2f2;
    --ink: #1a1a1a;
    --shadow-tone: #26282b;
  }
  * { margin: 0; padding: 0; box-sizing: border-box; }
  html, body { width: 942px; height: 1200px; overflow: hidden; }
  body { background: var(--backdrop); position: relative; }

  .brand-mark {
    position: absolute;
    display: flex; align-items: center; gap: 14px;
    font-family: "Cinzel", serif; font-weight: 600;
    color: var(--brand-brown);
    letter-spacing: 0.12em; line-height: 1.15; text-align: center;
  }
  .brand-mark__dot { border-radius: 50%; background: var(--brand-brown); flex: none; }

  .masthead-mark { left: 0; width: 942px; top: 118px; justify-content: center; font-size: 32px; }
  .masthead-mark .brand-mark__dot { width: 20px; height: 20px; }

  .bag-panel {
    position: absolute; top: 310px; height: 787px;
    background: var(--bag-black);
  }
  .bag-panel::after {
    content: ""; position: absolute; inset: 8px;
    border: 1px solid var(--keyline); pointer-events: none;
  }
  .bag-front { left: 88px; width: 296px; }
  .bag-back { left: 545px; width: 298px; }

  .continent-shade {
    position: absolute; left: 20px; right: 20px; bottom: 60px; height: 330px;
    background: radial-gradient(ellipse at 50% 45%, var(--shadow-tone) 0%, rgba(38,40,43,0) 70%);
  }

  .front-band {
    position: absolute; left: 0; right: 0; top: 158px; height: 57px;
    background: var(--band-blue);
  }
  .bag-front .brand-mark {
    left: 0; right: 0; top: 158px; height: 57px;
    justify-content: center; font-size: 16px;
  }
  .bag-front .brand-mark__dot { width: 11px; height: 11px; }

  .product-label { position: absolute; left: 32px; top: 323px; width: 232px; height: 290px; }
  .product-label svg { position: absolute; inset: 0; }
  .product-label__text { position: absolute; inset: 0; }
  .label-origin-pct {
    position: absolute; left: 0; right: 0; top: 34px; text-align: center;
    font-family: "Lato", sans-serif; font-weight: 700; font-size: 29px; color: var(--ink);
  }
  .label-origin {
    position: absolute; left: 0; right: 0; top: 68px; text-align: center;
    font-family: "Marcellus", serif; font-size: 25px; color: var(--ink); letter-spacing: 0.02em;
  }
  .label-roast {
    position: absolute;
    font-family: "Arimo", sans-serif; font-weight: 700; font-size: 53px; line-height: 1;
    color: var(--label-brown); letter-spacing: -0.01em;
  }
  .label-roast--dark { left: 66px; top: 116px; }
  .label-roast--roast { left: 28px; top: 162px; }
  .label-grind {
    position: absolute; left: 6px; right: 0; top: 218px; text-align: center;
    font-family: "Arimo", sans-serif; font-weight: 700; font-size: 21px; color: var(--label-brown);
  }

  .net-weight {
    position: absolute; left: 19px; bottom: 26px;
    font-family: "Marcellus", serif; font-size: 18px; color: var(--brand-brown);
  }

  .farm-story {
    position: absolute; left: 0; right: 0; top: 198px;
    font-family: "Cinzel", serif; font-weight: 400; font-size: 13.6px; line-height: 15.6px;
    color: var(--copy-white); text-align: center;
  }
  .bag-back .brand-mark {
    left: 0; right: 0; top: 608px; height: 60px;
    justify-content: center; font-size: 16px;
  }
  .bag-back .brand-mark__dot { width: 11px; height: 11px; }
</style>
</head>
<body>

  <div class="brand-mark masthead-mark">
    <span class="brand-mark__dot"></span>
    <span>Amber Ridge<br>Coffee</span>
  </div>

  <section class="bag-panel bag-front">
    <div class="continent-shade" role="img" aria-label="Faint map of Africa in dark grey"></div>
    <div class="front-band"></div>
    <div class="brand-mark">
      <span class="brand-mark__dot"></span>
      <span>Amber Ridge<br>Coffee</span>
    </div>

    <div class="product-label">
      <svg width="232" height="290" viewBox="0 0 232 290">
        <path d="M14 2 H218 A12 12 0 0 0 230 14 V276 A12 12 0 0 0 218 288 H14 A12 12 0 0 0 2 276 V14 A12 12 0 0 0 14 2 Z"
              fill="var(--label-white)" stroke="var(--label-brown)" stroke-width="3"/>
        <path d="M18 9 H214 A10 10 0 0 0 223 18 V272 A10 10 0 0 0 214 281 H18 A10 10 0 0 0 9 272 V18 A10 10 0 0 0 18 9 Z"
              fill="none" stroke="var(--label-brown)" stroke-width="1.2"/>
      </svg>
      <div class="product-label__text">
        <div class="label-origin-pct">100%</div>
        <div class="label-origin">TANZANIAN</div>
        <div class="label-roast label-roast--dark">Dark</div>
        <div class="label-roast label-roast--roast">Roast</div>
        <div class="label-grind">GROUND</div>
      </div>
    </div>

    <div class="net-weight">12oz</div>
  </section>

  <section class="bag-panel bag-back">
    <div class="continent-shade" role="img" aria-label="Faint map of Africa in dark grey"></div>
    <p class="farm-story">
      Amber Ridge Farms was<br>
      established in 1989 by<br>
      Marcus Ellery, son of<br>
      baseball legend Thomas<br>
      Ellery, and his family in<br>
      rural Tanzania.<br>
      Today the coffee brand is<br>
      sourced exclusively from the<br>
      Ellery farm and other<br>
      small scale family owned<br>
      farms in Tanzania and<br>
      East Africa.<br>
      This international coffee<br>
      initiative is designed to<br>
      bring a greater share of<br>
      coffee revenues to farmers<br>
      through direct trade<br>
      and help develop rural<br>
      communities in East Africa.
    </p>
    <div class="brand-mark">
      <span class="brand-mark__dot"></span>
      <span>Amber Ridge<br>Coffee</span>
    </div>
  </section>

</body>
</html>
```